Business Card Design

Please copy the format of the attached card.

FRONT:
White text small blue horses head logo where "mirano" in in example

BACK:
Blue background w/ white horses head

Industry/Entity Type

Business

Contact Information for Business Card

Dalton Greer
Chief Executive Officer
Tarnwick Inns & Resorts
417 Fenmore Street | San Francisco, California 94632
Tel: +1.310.555.0184
email: dalton@tarnwickinns-example.com

```html
<!DOCTYPE html>
<html lang="en">
<head>
<meta charset="utf-8">
<title>Dalton Greer – Business Card</title>
<link href="https://fonts.googleapis.com/css2?family=Questrial&display=swap" rel="stylesheet">
<style>
  :root {
    --page: #ffffff;
    --blue-deep: #0873aa;
    --blue-mid: #1793ce;
    --blue-light: #23a8e0;
    --ink: #ffffff;
  }
  * { margin: 0; padding: 0; box-sizing: border-box; }
  html, body {
    width: 1058px;
    height: 1200px;
    overflow: hidden;
    background: var(--page);
    font-family: "Questrial", "Century Gothic", sans-serif;
    color: var(--ink);
  }
  .canvas { position: relative; width: 1058px; height: 1200px; }
  .card {
    position: absolute;
    left: 4px;
    width: 1050px;
    background: linear-gradient(to bottom,
      var(--blue-deep) 0%,
      var(--blue-mid) 30%,
      var(--blue-light) 50%,
      var(--blue-mid) 72%,
      var(--blue-deep) 100%);
  }
  .card--front { top: 4px; height: 588px; }
  .card--back { top: 604px; height: 592px; }
  .line { position: absolute; white-space: nowrap; line-height: 1; }

  .front-brand {
    left: 0; width: 100%;
    top: 196px;
    text-align: center;
    font-size: 30px;
    letter-spacing: 0.5px;
  }
  .front-name {
    left: 0; width: 100%;
    top: 286px;
    padding-left: 20px;
    text-align: center;
    font-size: 56px;
    letter-spacing: -0.5px;
  }
  .front-title {
    left: 0; width: 100%;
    top: 344px;
    padding-left: 20px;
    text-align: center;
    font-size: 27px;
  }

  .contact { left: 42px; font-size: 33px; }
  .contact--address { top: 102px; }
  .contact--tel { top: 173px; }
  .contact--email { top: 244px; }

  .back-brand {
    right: 60px;
    top: 348px;
    font-size: 24px;
  }
  .back-name { left: 56px; top: 420px; font-size: 56px; letter-spacing: -0.5px; }
  .back-title { left: 56px; top: 480px; font-size: 35px; }
</style>
</head>
<body>
<div class="canvas">
  <section class="card card--front">
    <div class="line front-brand">Tarnwick Inns &amp; Resorts</div>
    <div class="line front-name">DALTON GREER</div>
    <div class="line front-title">Chief Executive Officer</div>
  </section>

  <section class="card card--back">
    <div class="line contact contact--address">417 Fenmore Street, San Francisco, California 94632</div>
    <div class="line contact contact--tel">Tel: 1.310.555.0184</div>
    <div class="line contact contact--email">Email: dalton@tarnwickinns-example.com</div>
    <div class="line back-brand">Tarnwick Inns &amp; Resorts</div>
    <div class="line back-name">DALTON GREER</div>
    <div class="line back-title">Chief Executive Officer</div>
  </section>
</div>
</body>
</html>
```